Batch #27 - MEN'S NATURAL THERAPEUTIC INTIMATE WASH

Men's Natural Therapeutic INTIMATE Wash
BATCH #27

Design a 4 oz. stand up tube with flip top cap...
To be packaged in a carton/box

Formula contains Tea Tree OIL
Aloe Vera Gel
Coconut Oil

PRODUCT IS A WASH/SOAP

Helps with
- Jock Itch (tinea cruris)
- Skin Rashes
- Candida
- Itchy Skin

COLORS ON TUBE: Gray, Black, Lime Electric Green and Blue

PRODUCT FOR MEN!

Target Market(s)

MEN

Industry/Entity Type

Retail

Font styles to use
Sans Serif

Colors
9bcb3b
abd036
33a6d7
000000
c9c9c9

Requirements
Must have
• Colors... black, gray, electric green and blue
Nice to have
• Needs to look masculine appeal to the male consumer

```html
<!DOCTYPE html>
<html lang="en">
<head>
<meta charset="utf-8">
<title>Batch #27 Wash/Soap – Tube and Carton</title>
<link rel="stylesheet" href="https://fonts.googleapis.com/css2?family=Michroma&family=Oswald:wght@400;500&family=Russo+One&display=swap">
<style>
  :root {
    --lime: #abd036;
    --lime-deep: #9bcb3b;
    --lime-pale: #d6ea8e;
    --black: #000000;
    --white: #ffffff;
    --gray-top: #8a8a8a;
    --gray-mid: #c9c9c9;
    --gray-bottom: #e8eef1;
  }
  * { margin: 0; padding: 0; box-sizing: border-box; }
  html, body { width: 1200px; height: 900px; overflow: hidden; }
  body {
    position: relative;
    background: linear-gradient(180deg, var(--gray-top) 0%, var(--gray-mid) 38%, var(--gray-bottom) 56%, var(--gray-bottom) 100%);
    font-family: "Oswald", sans-serif;
  }

  .shapes { position: absolute; left: 0; top: 0; width: 1200px; height: 900px; }

  .brand-name {
    position: absolute;
    font-family: "Michroma", sans-serif;
    color: var(--lime);
    line-height: 1;
    white-space: nowrap;
    text-align: right;
  }
  .brand-name.word { font-size: 37px; letter-spacing: 9px; margin-right: -9px; }
  .brand-name.number { font-size: 27px; letter-spacing: 4px; margin-right: -4px; }

  .product-type {
    position: absolute;
    font-family: "Russo One", sans-serif;
    color: var(--white);
    font-size: 19px;
    letter-spacing: 2px;
    line-height: 1;
    white-space: nowrap;
  }

  .list-title {
    position: absolute;
    font-style: italic;
    font-size: 16px;
    font-variant: small-caps;
    letter-spacing: 0.5px;
    line-height: 1;
  }
  .list {
    position: absolute;
    list-style: none;
    font-size: 21px;
    line-height: 23px;
    white-space: nowrap;
  }
  .list li::before { content: "• "; font-size: 15px; }

  .net-weight { position: absolute; line-height: 1; white-space: nowrap; }

  /* Tube label */
  .tube .word { right: 672px; top: 182px; }
  .tube .number { right: 676px; top: 222px; }
  .tube .product-type { right: 683px; top: 262px; }
  .contains-title { left: 252px; top: 332px; color: var(--white); }
  .contains-list { left: 249px; top: 351px; color: var(--lime); }
  .helps-title { left: 259px; top: 522px; color: var(--white); }
  .helps-list { left: 259px; top: 541px; color: var(--black); }
  .tube .net-weight { left: 354px; top: 692px; font-size: 20px; color: var(--black); }

  /* Carton front panel */
  .carton .word { right: 254px; top: 182px; }
  .carton .number { right: 254px; top: 222px; }
  .carton .product-type { right: 254px; top: 263px; }
  .carton .net-weight { left: 778px; top: 780px; font-size: 29px; color: var(--lime); }
</style>
</head>
<body>

  <svg class="shapes" viewBox="0 0 1200 900" aria-hidden="true">
    <defs>
      <pattern id="crimp-ridges" width="5" height="27" patternUnits="userSpaceOnUse">
        <rect width="5" height="27" fill="#abd036"/>
        <rect width="2" height="27" fill="#9bcb3b"/>
      </pattern>
      <linearGradient id="tube-dots" x1="0" y1="0" x2="1" y2="0">
        <stop offset="0" stop-color="#abd036" stop-opacity="0"/>
        <stop offset="1" stop-color="#abd036" stop-opacity="0.4"/>
      </linearGradient>
      <radialGradient id="carton-dots" cx="1" cy="0.55" r="0.9">
        <stop offset="0" stop-color="#abd036" stop-opacity="0.8"/>
        <stop offset="0.5" stop-color="#abd036" stop-opacity="0.3"/>
        <stop offset="1" stop-color="#abd036" stop-opacity="0"/>
      </radialGradient>
    </defs>

    <!-- tube -->
    <rect x="182" y="83" width="376" height="27" fill="url(#crimp-ridges)"/>
    <polygon points="182,110 558,110 510,448 226,448" fill="#000"/>
    <polygon role="img" aria-label="Lime halftone dot pattern fading in from the right edge"
             points="368,110 558,110 510,448 368,448" fill="url(#tube-dots)"/>
    <polygon points="226,448 510,448 509,456 227,456" fill="#abd036"/>
    <polygon points="227,456 509,456 508,464 228,464" fill="#000"/>
    <polygon points="228,464 508,464 484,712 256,712" fill="#abd036"/>
    <path d="M256,712 L484,712 L478,842 Q476,860 458,860 L280,860 Q263,860 262,842 Z" fill="#d6ea8e"/>

    <!-- carton -->
    <rect x="603" y="86" width="380" height="774" fill="#000"/>
    <rect x="632" y="86" width="10" height="774" fill="#abd036"/>
    <rect role="img" aria-label="Lime halftone dot pattern in the lower right corner"
          x="800" y="480" width="183" height="344" fill="url(#carton-dots)"/>
    <rect x="682" y="213" width="266" height="2" fill="#abd036"/>
    <rect x="852" y="250" width="96" height="2" fill="#abd036"/>

    <!-- tube rules -->
    <rect x="262" y="213" width="266" height="2" fill="#abd036"/>
  </svg>

  <section class="tube" aria-label="Tube label">
    <div class="brand-name word">BATCH</div>
    <div class="brand-name number">#27</div>
    <div class="product-type">WASH/SOAP</div>

    <div class="list-title contains-title">Contains:</div>
    <ul class="list contains-list">
      <li>Tea Tree OIL</li>
      <li>Aloe Vera Gel</li>
      <li>Coconut Oil</li>
    </ul>

    <div class="list-title helps-title">Helps with:</div>
    <ul class="list helps-list">
      <li>Jock Itch (tinea cruris)</li>
      <li>Skin Rashes</li>
      <li>Candida</li>
      <li>Itchy Skin</li>
    </ul>

    <div class="net-weight">4 oz</div>
  </section>

  <section class="carton" aria-label="Carton front panel">
    <div class="brand-name word">BATCH</div>
    <div class="brand-name number">#27</div>
    <div class="product-type">WASH/SOAP</div>
    <div class="net-weight">4 oz</div>
  </section>

</body>
</html>
```